STAND OUT BUSINESS CARD REQUIRED

I would like a business card that is going to be different and stand out!

Target Market(s)

Residential market, adults from 28yrs on

Industry/Entity Type

Electrician

Requirements
Must have
• Business name
• my name
• phone number
• email
• web address
• license no.
• abn
• fax no
• logo
Nice to have
• Extra info:
• FREE quotes
• Fixed pricing
• On time guarantee
• Life time labour Guarantee

```html
<!DOCTYPE html>
<html lang="en">
<head>
<meta charset="utf-8">
<title>Bright Spark Wiring – Business Card</title>
<link href="https://fonts.googleapis.com/css2?family=Ubuntu:wght@400;500;700&display=swap" rel="stylesheet">
<style>
  :root {
    --page: #ececec;
    --card-black: #141414;
    --card-dark: #262626;
    --orange: #f7941d;
    --orange-deep: #e8641b;
    --amber: #fbb034;
    --gold-light: #ffe27a;
    --gold: #e7b20f;
    --gold-dark: #a8740a;
    --white: #ffffff;
    --grey: #7a7a7a;
    --ink: #111111;
  }
  * { box-sizing: border-box; margin: 0; padding: 0; }
  html, body {
    width: 1200px; height: 873px; overflow: hidden;
    background: var(--page);
    font-family: "Ubuntu", sans-serif;
  }
  .card {
    position: absolute; top: 42px;
    width: 450px; height: 790px;
    border-radius: 6px; overflow: hidden;
    background: radial-gradient(ellipse at 50% 45%, var(--card-dark) 0%, var(--card-black) 70%);
    box-shadow: 0 4px 14px rgba(0,0,0,0.25);
  }
  .card--front { left: 130px; }
  .card--back { left: 620px; }

  /* Front */
  .hero-art {
    position: absolute; left: 0; top: 0; width: 450px; height: 330px;
    background:
      radial-gradient(circle at 50% 35%, var(--amber) 0%, var(--orange) 40%, var(--orange-deep) 70%, rgba(20,20,20,0) 100%);
  }
  .brand {
    position: absolute; left: 0; width: 450px; top: 330px;
    text-align: center; color: var(--orange);
    font-weight: 700; font-size: 34px; line-height: 1.1;
    text-transform: uppercase; letter-spacing: 0.5px;
  }
  .name-tab {
    position: absolute; left: 0; top: 440px; width: 380px; height: 58px;
  }
  .name-tab svg { position: absolute; left: 0; top: 0; }
  .name-tab .person {
    position: absolute; left: 24px; top: 4px;
    color: var(--ink); font-weight: 500; font-size: 27px;
  }
  .name-tab .role {
    position: absolute; left: 24px; top: 34px;
    color: var(--white); font-weight: 700; font-size: 17px; letter-spacing: 0.5px;
  }
  .contacts {
    position: absolute; left: 24px; top: 548px; list-style: none;
  }
  .contacts li {
    font-size: 21px; line-height: 35px; color: var(--white);
  }
  .contacts .label { color: var(--orange); font-weight: 500; }
  .legal {
    position: absolute; left: 24px; top: 714px;
    color: var(--grey); font-size: 16px; line-height: 26px;
  }

  /* Back */
  .promise {
    position: absolute; left: 0; width: 450px; text-align: center;
  }
  .promise svg { display: block; margin: 0 auto; }
  .promise p {
    color: var(--orange); font-size: 21px; line-height: 25px; margin-top: 8px;
  }
  .promise--pricing { top: 70px; }
  .promise--ontime { top: 288px; }
  .promise--labour { top: 515px; }
</style>
</head>
<body>
  <svg width="0" height="0" style="position:absolute">
    <defs>
      <radialGradient id="seal-gold" cx="40%" cy="35%" r="70%">
        <stop offset="0%" stop-color="#ffe27a"/>
        <stop offset="55%" stop-color="#e7b20f"/>
        <stop offset="100%" stop-color="#a8740a"/>
      </radialGradient>
    </defs>
  </svg>

  <section class="card card--front">
    <div class="hero-art" role="img" aria-label="Cartoon electrician superhero holding a light bulb over an orange sunburst"></div>
    <div class="brand">Bright Spark<br>Wiring Pty Ltd</div>

    <div class="name-tab">
      <svg width="380" height="58" viewBox="0 0 380 58" aria-hidden="true">
        <polygon points="0,0 345,0 380,29 345,58 0,58" fill="var(--orange)"/>
        <polygon points="0,33 358,33 345,58 0,58" fill="var(--orange-deep)"/>
      </svg>
      <span class="person">Daniel Moore</span>
      <span class="role">DIRECTOR</span>
    </div>

    <ul class="contacts">
      <li><span class="label">phone:</span> 0412 555 019</li>
      <li><span class="label">fax:</span> 02 5550 1234</li>
      <li><span class="label">email:</span> info@brightsparkwiring.com.au</li>
      <li><span class="label">web:</span> www.brightsparkwiring.com.au</li>
    </ul>

    <div class="legal">
      license no.: 318452K<br>
      ABN: 27 394 815 306
    </div>
  </section>

  <section class="card card--back">
    <div class="promise promise--pricing">
      <svg width="170" height="170" viewBox="0 0 170 170" aria-hidden="true">
        <circle cx="85" cy="85" r="82" fill="url(#seal-gold)"/>
        <circle cx="85" cy="85" r="62" fill="none" stroke="#a8740a" stroke-width="3"/>
      </svg>
      <p>Fixed Pricing</p>
    </div>

    <div class="promise promise--ontime">
      <svg width="170" height="170" viewBox="0 0 170 170" aria-hidden="true">
        <circle cx="85" cy="85" r="82" fill="url(#seal-gold)"/>
        <circle cx="85" cy="85" r="62" fill="none" stroke="#a8740a" stroke-width="3"/>
        <circle cx="85" cy="85" r="36" fill="none" stroke="#a8740a" stroke-width="6"/>
        <polyline points="85,62 85,85 100,97" fill="none" stroke="#a8740a" stroke-width="6" stroke-linecap="round"/>
      </svg>
      <p>On Time<br>Guarantee</p>
    </div>

    <div class="promise promise--labour">
      <svg width="170" height="170" viewBox="0 0 170 170" aria-hidden="true">
        <circle cx="85" cy="85" r="82" fill="url(#seal-gold)"/>
        <circle cx="85" cy="85" r="62" fill="none" stroke="#a8740a" stroke-width="3"/>
        <line x1="62" y1="108" x2="100" y2="70" stroke="#a8740a" stroke-width="10" stroke-linecap="round"/>
        <circle cx="106" cy="64" r="14" fill="none" stroke="#a8740a" stroke-width="7"/>
      </svg>
      <p>Lifetime Labour<br>Guarantee</p>
    </div>
  </section>
</body>
</html>
```